Upscale business cards needed for family office

We would like professional business cards created for employees of our family office. Relatively simple and straightforward, but also with a unique element to set them apart. Probably stick with neutral and simple colors that mesh well with the colors in the logo. We need space for the traditional elements, including name, title, address, email/phone number.

Industry/Entity Type

Business

Contact Information for Business Card

Space for name, title, phone number, email, address

```html
<!DOCTYPE html>
<html lang="en">
<head>
<meta charset="utf-8">
<title>R&amp;L Business Card</title>
<link rel="stylesheet" href="https://fonts.googleapis.com/css2?family=Lato:wght@700;900&family=Arimo:wght@400&display=swap">
<style>
  :root {
    --backdrop: #2e2e2e;
    --card: #f4f4f4;
    --ink: #3a3a3a;
    --accent: #1a7fae;
    --accent-light: #2ba6c9;
    --logo-frame: #8a8f94;
  }
  * { margin: 0; padding: 0; box-sizing: border-box; }
  html, body { width: 1200px; height: 997px; overflow: hidden; }
  body {
    background: var(--backdrop);
    position: relative;
    font-family: "Arimo", Arial, sans-serif;
  }
  .business-card {
    position: absolute;
    left: 170px;
    top: 254px;
    width: 860px;
    height: 490px;
    background: linear-gradient(160deg, #ffffff 0%, var(--card) 60%, #e6e6e6 100%);
    border-radius: 24px;
  }
  .brand-mark {
    position: absolute;
    right: 48px;
    top: 42px;
    display: flex;
    align-items: center;
    gap: 12px;
  }
  .brand-square {
    width: 22px;
    height: 22px;
    background: var(--accent);
  }
  .brand-name {
    font-family: "Lato", sans-serif;
    font-weight: 700;
    font-size: 36px;
    color: var(--ink);
  }
  .name-row {
    position: absolute;
    left: 66px;
    right: 48px;
    top: 228px;
    display: flex;
    align-items: flex-end;
    gap: 10px;
  }
  .person-name {
    font-family: "Lato", sans-serif;
    font-weight: 900;
    font-size: 30px;
    color: var(--ink);
    white-space: nowrap;
    line-height: 1;
  }
  .divider {
    flex: 1;
    height: 2px;
    background: var(--accent);
    margin-bottom: 3px;
  }
  .person-title {
    position: absolute;
    left: 68px;
    top: 266px;
    font-family: "Lato", sans-serif;
    font-weight: 700;
    font-size: 17px;
    letter-spacing: 0.5px;
    color: var(--accent);
  }
  .web-address {
    position: absolute;
    right: 48px;
    top: 282px;
    font-family: "Lato", sans-serif;
    font-weight: 700;
    font-size: 19px;
    color: var(--accent);
  }
  .contact-list {
    position: absolute;
    left: 70px;
    top: 320px;
    list-style: none;
  }
  .contact-item {
    display: flex;
    align-items: flex-start;
    gap: 14px;
    font-size: 19px;
    line-height: 24px;
    color: var(--ink);
    margin-bottom: 14px;
  }
  .contact-icon {
    flex: none;
    width: 22px;
    height: 22px;
    margin-top: 1px;
  }
</style>
</head>
<body>
  <div class="business-card">
    <div class="brand-mark">
      <span class="brand-square"></span>
      <span class="brand-name">R&amp;L</span>
    </div>

    <div class="name-row">
      <span class="person-name">Clara Whitfield</span>
      <span class="divider"></span>
    </div>
    <div class="person-title">FOUNDER &amp; CEO</div>
    <div class="web-address">www.rlholdings.com</div>

    <ul class="contact-list">
      <li class="contact-item">
        <svg class="contact-icon" viewBox="0 0 22 22" aria-hidden="true">
          <circle cx="11" cy="11" r="11" fill="var(--accent-light)"/>
          <path d="M7 8.5c0-1 1-1.6 1.8-1.2l.8.4-.6 2 -1 .5c.6 1.4 1.6 2.4 3 3l.5-1 2-.6.4.8c.4.8-.2 1.8-1.2 1.8C9.6 14.2 7 11.6 7 8.5z" fill="#fff"/>
        </svg>
        <span>+1 (555) 014-2290</span>
      </li>
      <li class="contact-item">
        <svg class="contact-icon" viewBox="0 0 22 22" aria-hidden="true">
          <circle cx="11" cy="11" r="11" fill="var(--accent-light)"/>
          <path d="M11 5.5l5.5 5h-1.6V16h-2.6v-3.4H9.7V16H7.1v-5.5H5.5z" fill="#fff"/>
        </svg>
        <span>www.rlholdings.com</span>
      </li>
      <li class="contact-item">
        <svg class="contact-icon" viewBox="0 0 22 22" aria-hidden="true">
          <circle cx="11" cy="11" r="11" fill="var(--accent-light)"/>
          <path d="M11 5a3.8 3.8 0 0 0-3.8 3.8c0 2.8 3.8 7.2 3.8 7.2s3.8-4.4 3.8-7.2A3.8 3.8 0 0 0 11 5zm0 5.2a1.4 1.4 0 1 1 0-2.8 1.4 1.4 0 0 1 0 2.8z" fill="#fff"/>
        </svg>
        <span>42 Harbor View Road, 2nd Floor,<br>Westport, CT 06880</span>
      </li>
    </ul>
  </div>
</body>
</html>
```